Make a creative business cards for our agency

We are a creative, digital marketing and IT development agency. We need a new: flat design, modern-corporate, not much elements, two sided business cards based in our logo (which I provide here in jpg and psd).

We prefer a vertical design, please no, qr codes no complex backgrounds, NO TEMPLATES.

We want to include:

Logo/Name of the agency
Slogan
Name
Title
Email
Phone
Web url
Social Media (Facebook, Twitter and Youtube)
You can simulate all this info and just place invented info.

Feel free to propose. Very important is to keep the same dark red color of the logo for a big area in the background of your design, keep the same font type preferably, you can get off of the box I you consider your idea is great.

In the case you need extra material or more brief info, just let me know please.

```html
<!DOCTYPE html>
<html lang="en">
<head>
<meta charset="utf-8">
<title>Ridgeway Studio – Business Cards</title>
<link rel="stylesheet" href="https://fonts.googleapis.com/css2?family=Raleway:wght@400;500&display=swap">
<style>
  :root {
    --brand-red: #8a1114;
    --card-white: #ffffff;
    --ink: #2b2b2b;
    --ink-soft: #e6d6d6;
    --stage: #2c2f33;
  }
  * { margin: 0; padding: 0; box-sizing: border-box; }
  html, body { width: 1200px; height: 900px; overflow: hidden; }
  body {
    background: var(--stage);
    font-family: "Raleway", sans-serif;
    position: relative;
  }
  .card {
    position: absolute;
    width: 340px;
    height: 595px;
    border-radius: 20px;
    overflow: hidden;
    background: var(--card-white);
  }
  .card--back { left: 220px; top: 152px; }
  .card--front { left: 640px; top: 152px; }
  .card__shape { position: absolute; inset: 0; width: 100%; height: 100%; }

  .brand { position: absolute; color: var(--card-white); }
  .brand__row { display: flex; align-items: center; gap: 12px; }
  .brand__dot {
    width: 24px; height: 24px; border-radius: 50%;
    background: var(--card-white); flex: none;
  }
  .brand__name { font-weight: 400; font-size: 28px; letter-spacing: 0.3px; white-space: nowrap; }
  .brand__slogan { font-weight: 400; font-size: 12.5px; margin-top: 8px; color: var(--ink-soft); letter-spacing: 0.3px; }

  .card--back .brand { left: 34px; top: 80px; }
  .card--front .brand { left: 0; right: 0; top: 250px; text-align: center; }
  .card--front .brand__row { justify-content: center; }
  .card--front .brand__name { font-size: 30px; }
  .card--front .brand__slogan { font-size: 14px; }

  .contact-list {
    position: absolute;
    left: 34px; bottom: 54px;
    list-style: none;
    color: var(--ink);
    font-weight: 500;
    font-size: 14px;
  }
  .contact-list li { display: flex; align-items: center; gap: 12px; height: 25px; }
  .contact-icon { width: 16px; height: 16px; flex: none; }
</style>
</head>
<body>

  <section class="card card--back" aria-label="Business card, contact side">
    <svg class="card__shape" viewBox="0 0 340 595" aria-hidden="true">
      <polygon points="0,0 340,0 340,285 0,375" fill="var(--brand-red)"/>
    </svg>
    <div class="brand">
      <div class="brand__row"><span class="brand__dot"></span><span class="brand__name">Ridgeway Studio</span></div>
      <p class="brand__slogan">Design, Code, Brand &amp; Growth</p>
    </div>
    <ul class="contact-list">
      <li>
        <svg class="contact-icon" viewBox="0 0 16 16" aria-hidden="true"><rect x="1" y="3" width="14" height="10" rx="1.5" fill="var(--ink)"/><polyline points="2,4.5 8,9 14,4.5" fill="none" stroke="#fff" stroke-width="1.3"/></svg>
        <span>hello@ridgewaystudio.com</span>
      </li>
      <li>
        <svg class="contact-icon" viewBox="0 0 16 16" aria-hidden="true"><path d="M4 1.5l2.5 3-1.5 1.8c.8 1.8 2.4 3.4 4.2 4.2L11 9l3 2.5-1.5 2.8C7 14 2 9 1.6 3.1z" fill="var(--ink)"/></svg>
        <span>+1 555 0134 728</span>
      </li>
      <li>
        <svg class="contact-icon" viewBox="0 0 16 16" aria-hidden="true"><circle cx="8" cy="8" r="6.5" fill="none" stroke="var(--ink)" stroke-width="1.4"/><ellipse cx="8" cy="8" rx="2.8" ry="6.5" fill="none" stroke="var(--ink)" stroke-width="1.2"/><line x1="1.5" y1="8" x2="14.5" y2="8" stroke="var(--ink)" stroke-width="1.2"/></svg>
        <span>www.ridgewaystudio.com</span>
      </li>
      <li>
        <svg class="contact-icon" viewBox="0 0 16 16" aria-hidden="true"><circle cx="8" cy="8" r="7" fill="var(--ink)"/></svg>
        <span>www.clipstream.com</span>
      </li>
      <li>
        <svg class="contact-icon" viewBox="0 0 16 16" aria-hidden="true"><circle cx="8" cy="8" r="7" fill="var(--ink)"/></svg>
        <span>www.friendsbook.com</span>
      </li>
      <li>
        <svg class="contact-icon" viewBox="0 0 16 16" aria-hidden="true"><circle cx="8" cy="8" r="7" fill="var(--ink)"/></svg>
        <span>www.chirpline.com</span>
      </li>
    </ul>
  </section>

  <section class="card card--front" aria-label="Business card, logo side">
    <svg class="card__shape" viewBox="0 0 340 595" aria-hidden="true">
      <circle cx="160" cy="280" r="305" fill="var(--brand-red)"/>
    </svg>
    <div class="brand">
      <div class="brand__row"><span class="brand__dot"></span><span class="brand__name">Ridgeway Studio</span></div>
      <p class="brand__slogan">Design, Code, Brand &amp; Growth</p>
    </div>
  </section>

</body>
</html>
```